Graphic for social media

I woudl liek you to create an graphic highlighting that I was voted "Best Lawyer, Runner Up" by BayPulse Magazine and I was also named to "Top Counsel Across America" Include our website www.kendrelpartners.com. INclude my name, Miles Kendrel, by my photo.

```html
<!DOCTYPE html>
<html lang="en">
<head>
<meta charset="utf-8">
<title>Miles Kendrel – Award Graphic</title>
<link rel="stylesheet" href="https://fonts.googleapis.com/css2?family=Cinzel:wght@500&family=Didact+Gothic&family=Italiana&family=Quicksand:wght@400&family=Montserrat:wght@600&display=swap">
<style>
  :root {
    --bg-dark: #1b1e26;
    --card: #ffffff;
    --band-black: #050505;
    --gold: #a88a52;
    --gold-bright: #d9a232;
    --ink: #474747;
    --badge-blue: #2ba6de;
    --badge-border: #8a8a8a;
    --white: #ffffff;
  }
  * { margin: 0; padding: 0; box-sizing: border-box; }
  html, body { width: 1200px; height: 1200px; overflow: hidden; background: var(--bg-dark); }
  .canvas { position: relative; width: 1200px; height: 1200px; background: var(--bg-dark); }
  .card { position: absolute; left: 145px; top: 147px; width: 915px; height: 914px; background: var(--card); }

  .firm-band { position: absolute; left: 145px; top: 206px; width: 529px; height: 146px; background: var(--band-black); }
  .firm-mark { position: absolute; left: 60px; top: 36px; width: 74px; height: 74px; background: var(--gold-bright); }
  .firm-name { position: absolute; left: 146px; top: 50px; font-family: "Cinzel", serif; font-weight: 500; font-size: 25px; color: var(--white); white-space: nowrap; letter-spacing: 0.5px; }
  .firm-tagline { position: absolute; left: 146px; top: 87px; width: 302px; display: flex; align-items: center; gap: 6px; font-family: "Montserrat", sans-serif; font-weight: 600; font-size: 11px; letter-spacing: 5.5px; color: var(--white); white-space: nowrap; }
  .firm-tagline::before, .firm-tagline::after { content: ""; flex: 1; height: 1px; background: var(--white); }

  .attorney-name { position: absolute; left: 194px; top: 418px; font-family: "Italiana", sans-serif; font-size: 76px; line-height: 1; color: var(--ink); white-space: nowrap; }
  .name-rule { position: absolute; left: 190px; top: 512px; width: 458px; height: 5px; background: var(--gold); }

  .honor { position: absolute; left: 190px; height: 53px; padding-left: 15px; border-left: 4px solid var(--gold); font-family: "Didact Gothic", sans-serif; font-size: 40px; line-height: 53px; color: var(--ink); white-space: nowrap; }
  .honor-runner-up { top: 550px; }
  .honor-top-counsel { top: 626px; font-size: 36px; }

  .badge-strip { position: absolute; left: 145px; top: 719px; width: 410px; height: 101px; background: var(--card); box-shadow: 0 6px 8px rgba(0,0,0,0.18); }
  .badge-listing { position: absolute; left: 33px; top: 14px; width: 224px; height: 76px; border: 1px solid var(--badge-border); background: var(--white); }
  .badge-magazine { position: absolute; left: 290px; top: 1px; width: 96px; height: 96px; border-radius: 50%; background: var(--badge-blue); }

  .portrait { position: absolute; left: 683px; top: 206px; width: 377px; height: 636px; }

  .url-band { position: absolute; left: 502px; top: 842px; width: 558px; height: 102px; background: var(--gold); display: flex; align-items: center; justify-content: center; }
  .url { font-family: "Quicksand", sans-serif; font-weight: 400; font-size: 32px; color: var(--white); letter-spacing: 1px; white-space: nowrap; }
</style>
</head>
<body>
<main class="canvas">
  <div class="card"></div>

  <header class="firm-band">
    <span class="firm-mark"></span>
    <div class="firm-name">KENDREL PARTNERS, PLLC</div>
    <div class="firm-tagline">Attorneys At Law</div>
  </header>

  <h1 class="attorney-name">Miles Kendrel</h1>
  <div class="name-rule"></div>

  <p class="honor honor-runner-up">Best Lawyer, Runner Up</p>
  <p class="honor honor-top-counsel">Top Counsel Across America</p>

  <div class="badge-strip">
    <div class="badge-listing" role="img" aria-label="Recognition listing badge"></div>
    <div class="badge-magazine" role="img" aria-label="BayPulse Magazine award badge"></div>
  </div>

  <svg class="portrait" viewBox="0 0 377 636" role="img" aria-label="Portrait photo of Miles Kendrel in a dark suit and gold tie">
    <defs>
      <linearGradient id="portraitTone" x1="0" y1="0" x2="0" y2="1">
        <stop offset="0" stop-color="#f6f4f2"/>
        <stop offset="0.35" stop-color="#b98a6a"/>
        <stop offset="0.6" stop-color="#3a2a24"/>
        <stop offset="1" stop-color="#1c1a1a"/>
      </linearGradient>
      <filter id="archShadow" x="-10%" y="-10%" width="120%" height="120%">
        <feDropShadow dx="-3" dy="0" stdDeviation="4" flood-opacity="0.18"/>
      </filter>
    </defs>
    <path d="M0 636 V309 A377 309 0 0 1 377 0 V636 Z" fill="url(#portraitTone)" filter="url(#archShadow)"/>
  </svg>

  <div class="url-band">
    <span class="url">www.kendrelpartners.com.</span>
  </div>
</main>
</body>
</html>
```